Flyer PRTW

Everyone deserves true happiness.
Real Food is the answer to:
A body you love
Reverting illnesses
Healthy digestion
Stable blood sugar
Emotions in control
Blasting energy
Sound sleep
REAL food + water + exercise + Laughter =
“HIGH QUALITY OF LIFE “
EASY, right?
Challenging: certainly
Changing habits: reluctance in sight!
WE’RE OFFER TO:
1. Study YOUR unique body composition, food cravings, blockages, illnesses, and personality!
2. Introduce you to new Food
3. customized wellness plan with follow ups
4. meditation,cooking, and fitness classes as well as wellness workshops
5. New friends with high aspirations
LOGO
Contact info
Please visit our web address to see our design style and colors: www.pinerivertallwave.net
Target Market(s)
people who want to be more healthy
Industry/Entity Type
Fitness
Requirements
Must have
- beautiful pictures of fresh food (main picture) and maybe a few more small pictures reflecting
exercise
healthy living
meditation
Nice to have
- look is crucial. recall some of the color or colors from my logo to have a theme

```html
<!DOCTYPE html>
<html lang="en">
<head>
<meta charset="utf-8">
<title>Pinerivertallwave Flyer</title>
<link href="https://fonts.googleapis.com/css2?family=Questrial&family=Open+Sans:wght@400;700&family=Lora:ital@1&family=Patrick+Hand&display=swap" rel="stylesheet">
<style>
  :root {
    --page: #ffffff;
    --panel: #fbe89b;
    --panel-edge: #e6cf72;
    --box: #fdf4c9;
    --box-edge: #c7b25a;
    --red: #d2391d;
    --green: #3e7a1f;
    --leaf: #6aa82b;
    --brown: #4a3f24;
    --text-soft: #4c6b2a;
  }
  * { box-sizing: border-box; margin: 0; padding: 0; }
  html, body { width: 1200px; height: 2400px; overflow: hidden; background: var(--page); }
  .canvas { position: relative; width: 1200px; height: 2400px; }

  .panel {
    position: absolute; left: 30px; width: 1140px;
    background: var(--panel);
    border: 2px solid var(--panel-edge);
    box-shadow: 8px 10px 14px rgba(0,0,0,.35);
  }
  .panel--outside { top: 20px; height: 1125px; }
  .panel--inside { top: 1235px; height: 1145px; }

  .box {
    position: absolute;
    background: var(--box);
    border: 2px solid var(--box-edge);
    box-shadow: 2px 3px 6px rgba(0,0,0,.18);
  }

  /* Outside panel */
  .testimonials { left: 68px; top: 78px; width: 500px; height: 690px; padding: 30px 30px; text-align: center; }
  .quote { font-family: "Lora", serif; font-style: italic; font-size: 19px; line-height: 1.32; color: var(--text-soft); }
  .quote-author { font-family: "Questrial", sans-serif; font-size: 18px; color: var(--text-soft); margin: 14px 0 28px; }

  .brand-small { position: absolute; left: 68px; top: 880px; width: 500px; display: flex; align-items: center; justify-content: center; gap: 16px; }
  .brand-small .dot { width: 70px; height: 70px; border-radius: 50%; background: var(--leaf); flex: none; }
  .brand-small .name { font-family: "Questrial", sans-serif; font-size: 44px; color: var(--brown); line-height: 1; }
  .brand-small .tag { font-family: "Questrial", sans-serif; font-size: 12.5px; color: var(--green); letter-spacing: 1px; margin-top: 6px; }

  .contact { position: absolute; left: 68px; top: 990px; width: 500px; text-align: center; font-family: "Open Sans", sans-serif; color: var(--green); font-size: 19px; line-height: 1.45; }
  .contact h3 { font-size: 22px; font-weight: 700; margin-bottom: 10px; }

  .photo-strip { left: 610px; top: 130px; width: 250px; height: 900px; padding: 20px 18px; display: flex; flex-direction: column; gap: 18px; }
  .photo { flex: 1; border: 3px solid #ffffff; outline: 1px solid var(--box-edge); }
  .photo--jump { background: linear-gradient(180deg, #3d7fd0 0%, #9cc7ef 55%, #5f9d2c 80%, #3f7a1f 100%); }
  .photo--produce { background: linear-gradient(135deg, #7a4a25 0%, #c0392b 35%, #6a9a2a 65%, #e0a020 100%); }
  .photo--meditate { background: linear-gradient(160deg, #5a9a2c 0%, #9bc65a 50%, #e8e4da 100%); }
  .photo--stretch { background: linear-gradient(150deg, #f0e6dc 0%, #c98a60 45%, #e24a3a 75%, #f3d9c9 100%); }

  .title-vertical { position: absolute; left: 1010px; top: 40px; height: 1080px; writing-mode: vertical-rl; font-family: "Questrial", sans-serif; font-size: 104px; line-height: 1; color: var(--brown); letter-spacing: 1px; }
  .subtitle-vertical { position: absolute; left: 955px; top: 50px; writing-mode: vertical-rl; font-family: "Questrial", sans-serif; font-size: 29px; letter-spacing: 4px; color: var(--brown); }

  /* Inside panel */
  .benefits { left: 50px; top: 65px; width: 476px; height: 790px; padding: 26px 32px; }
  .offer { left: 634px; top: 65px; width: 476px; height: 790px; padding: 26px 30px; }
  .heading { font-family: "Open Sans", sans-serif; font-weight: 700; color: var(--red); font-size: 35px; text-align: center; line-height: 1.2; margin-bottom: 20px; }
  .lead { font-family: "Open Sans", sans-serif; font-weight: 700; color: var(--green); font-size: 22px; margin-bottom: 18px; }
  .list { list-style: none; font-family: "Open Sans", sans-serif; font-weight: 700; color: var(--green); font-size: 22px; }
  .list li { position: relative; padding-left: 40px; margin-bottom: 26px; line-height: 1.35; }
  .list li::before { content: ""; position: absolute; left: 6px; top: 11px; width: 9px; height: 9px; border-radius: 50%; background: var(--green); }
  .offer .lead { font-size: 20px; margin-bottom: 14px; }
  .offer .list { font-size: 20px; }
  .offer .list li { margin-bottom: 22px; padding-left: 34px; }
  .offer .list li::before { top: 10px; }
  .equation { font-family: "Patrick Hand", sans-serif; color: var(--red); font-size: 28px; text-align: center; line-height: 1.3; letter-spacing: 1px; }
  .equation .result { font-size: 31px; }
  .pair { font-family: "Open Sans", sans-serif; font-weight: 700; color: var(--green); font-size: 20px; margin-bottom: 18px; line-height: 1.5; }
  .pair span { display: block; font-weight: 400; padding-left: 100px; }

  .brand-large { position: absolute; left: 60px; top: 905px; display: flex; align-items: center; gap: 30px; }
  .brand-large .dot { width: 200px; height: 200px; border-radius: 50%; background: var(--leaf); flex: none; }
  .brand-large .name { font-family: "Questrial", sans-serif; font-size: 92px; color: var(--brown); line-height: 1; }
  .brand-large .tag { font-family: "Questrial", sans-serif; font-size: 31px; color: var(--green); letter-spacing: 2px; margin-top: 14px; }
</style>
</head>
<body>
<main class="canvas">

  <section class="panel panel--outside">
    <div class="box testimonials">
      <p class="quote">“Since Marisol has been providing me with nutrition coaching, her positivity &amp; desire to help have made a difference in my life motivating me to continue my journey. She constantly offers ideas to eat better &amp; has even created a list of all the good snacks we can have when a craving hits. She is personally interested in making a difference in my life and always ready when I need her. Although this is just the beginning, I know that with her on my side this journey will be great!”</p>
      <p class="quote-author">Danielle K., Office Manager, Cedar Point</p>
      <p class="quote">“I came to Marisol during a very crucial life change. I found her to be patient, kind, enthusiastic, honest, helpful &amp; most importantly a wonderful listener. Marisol was able to create a nutrition guide suitable even for my picky eating habits. I have learned to introduce new fruits and vegetables into my palate &amp; wouldn’t have thought of doing so without Marisol’s suggestions of different cooking methods. Marisol inspires me to be healthier &amp; for that I am forever grateful.”</p>
      <p class="quote-author">Marcus L. –pre-sales, Brookfield, ST</p>
    </div>

    <div class="brand-small">
      <span class="dot"></span>
      <div>
        <div class="name">Pinerivertallwave</div>
        <div class="tag">BALANCED NUTRITION, MIND, AND FITNESS</div>
      </div>
    </div>

    <div class="contact">
      <h3>Contact:</h3>
      <p>Phone: (555) 014-2276</p>
      <p>Email: marisol@pinerivertallwave.net</p>
      <p>www.pinerivertallwave.net</p>
    </div>

    <div class="box photo-strip">
      <div class="photo photo--jump" role="img" aria-label="Photo of a person leaping joyfully over a green field under a blue sky"></div>
      <div class="photo photo--produce" role="img" aria-label="Photo of a crate of fresh fruits and vegetables"></div>
      <div class="photo photo--meditate" role="img" aria-label="Photo of a person meditating on green grass"></div>
      <div class="photo photo--stretch" role="img" aria-label="Photo of two women stretching together in a fitness class"></div>
    </div>

    <div class="subtitle-vertical">BALANCED NUTRITION, MIND, AND FITNESS</div>
    <div class="title-vertical">Pinerivertallwave</div>
  </section>

  <section class="panel panel--inside">
    <div class="box benefits">
      <h2 class="heading">EVERYONE DESERVES<br>TRUE HAPPINESS</h2>
      <p class="lead">REAL Food is the answer to:</p>
      <ul class="list">
        <li>A body you love</li>
        <li>Reverting illnesses</li>
        <li>Healthy digestion</li>
        <li>Stable blood sugar</li>
        <li>Emotions in control</li>
        <li>Blasting energy</li>
        <li>Sound sleep</li>
      </ul>
      <p class="equation">REAL food<br>+<br>water + exercise + laughter<br>=<br><span class="result">“HIGH QUALITY OF LIFE”</span></p>
    </div>

    <div class="box offer">
      <h2 class="heading">EASY, RIGHT?</h2>
      <p class="pair">Challenging:<span>certainly</span></p>
      <p class="pair">Changing habits:<span>reluctance in sight!</span></p>
      <p class="lead">WE’RE TO OFFER:</p>
      <ul class="list">
        <li>Study YOUR unique body composition, food cravings, blockages, illnesses, and personality!</li>
        <li>Introduce you to new food.</li>
        <li>Customized wellness plan with follow ups.</li>
        <li>Meditation, cooking, and fitness classes as well as wellness workshops.</li>
        <li>New friends with high aspirations.</li>
      </ul>
    </div>

    <div class="brand-large">
      <span class="dot"></span>
      <div>
        <div class="name">Pinerivertallwave</div>
        <div class="tag">BALANCED NUTRITION, MIND, AND FITNESS</div>
      </div>
    </div>
  </section>

</main>
</body>
</html>
```